Registration Mailer Templates for Student Travel Company

I need WORD templates for registration marketing/mailing to solicit target audience to sign up for class trip. Need (2) pages (8.5 x 11) front & back, so 4 designs total, able to be customized and editable copy without changing the branding, design or color scheme. See branding guidelines and page template guidelines attached. see uploaded files. And design must utilize all print areas.

Target Market(s)

13-17 yeard old studenst and parents, and middle school teachers

Industry/Entity Type

educational student travel

Font styles to use
Other font styles liked:
• See branding guidelines page attached

Requirements
Must have
• 2 pages, front and back design, so 4 total page designs, simple design, professional
Should not have
• no airplanes or buses in design

```html
<!DOCTYPE html>
<html lang="en">
<head>
<meta charset="utf-8">
<title>Summit Trails – Registration Mailer Pages</title>
<link href="https://fonts.googleapis.com/css2?family=Open+Sans:wght@400;600;700&family=Oswald:wght@300;500&display=swap" rel="stylesheet">
<style>
:root{
  --ink:#1f3547;
  --body:#2c4a5c;
  --teal:#6bb5a6;
  --green:#8cc65a;
  --blue:#2f9bd6;
  --band:#4a8fd2;
  --line:#333;
  --black:#000;
  --white:#fff;
}
*{box-sizing:border-box;margin:0;padding:0}
html,body{width:1200px;height:3927px;overflow:hidden;background:var(--black)}
body{position:relative;font-family:"Open Sans",Arial,sans-serif;color:var(--body)}
.page{position:absolute;background:var(--white);overflow:hidden}
.stripe{position:absolute;left:0;top:0;background:linear-gradient(180deg,var(--teal),var(--green))}
.page-label{position:absolute;color:var(--white);font-weight:700;font-size:25px;letter-spacing:.5px;text-align:center;white-space:nowrap}
.brand{position:absolute;display:flex;align-items:center;gap:10px;font-weight:700;color:var(--ink);letter-spacing:3px;line-height:1}
.brand-mark{background:var(--blue);display:block}
.lorem{font-size:15px;line-height:22px;color:var(--body)}
.lorem + .lorem{margin-top:22px}
/* page 1 */
.p1{left:15px;top:15px;width:1098px;height:848px}
.p1 .stripe{width:46px;height:100%}
.letter-title{position:absolute;left:107px;top:126px;font-size:22px;font-weight:600;color:var(--ink)}
.letter-salute{position:absolute;left:107px;top:170px;font-size:17px;font-weight:600;color:var(--ink)}
.letter-body{position:absolute;left:107px;top:206px;width:950px}
.letter-sign{position:absolute;left:107px;top:455px;font-size:16px;line-height:24px;color:var(--ink)}
.info{position:absolute;width:260px}
.info svg{display:block;width:62px;height:62px;margin-bottom:10px}
.info h3{font-size:15px;font-weight:700;color:var(--ink)}
.info p{font-size:14px;line-height:18px;color:var(--body)}
/* page 2 */
.p2{left:15px;top:991px;width:697px;height:900px}
.p2 .stripe{width:81px;height:100%}
.itin-title{position:absolute;left:96px;top:60px;width:586px;text-align:center;font-size:10px;font-weight:600;color:var(--ink)}
.itin{position:absolute;left:96px;top:76px;width:586px;height:400px;border:1px solid var(--line);border-collapse:collapse;table-layout:fixed;font-size:7.4px;line-height:9px;color:#222}
.itin th{background:#e9e9e9;border:1px solid var(--line);height:14px;font-size:8.5px}
.itin td{border:1px solid var(--line);vertical-align:top;padding:10px 4px}
.itin td p{margin-bottom:9px}
.itin .c{text-align:center}
.itin b{font-weight:700}
.itin .note{border:1px solid var(--line);padding:5px;margin-top:22px}
.disclaimer{position:absolute;left:96px;top:505px;width:580px}
.disclaimer h2{font-size:14px;font-weight:700;color:var(--ink);margin-bottom:4px}
.disclaimer p{font-size:12.3px;line-height:16px;margin-bottom:16px}
.disclaimer p.gap{margin-bottom:34px}
/* page 3 */
.p3{left:15px;top:1938px;width:1118px;height:862px}
.p3 .stripe,.p4 .stripe{width:46px;height:449px}
.dots{position:absolute;left:0;width:100%;border-top:3px dotted #555}
.trip-col{position:absolute;top:150px;width:475px}
.trip-col h2{font-size:20px;font-weight:700;color:var(--blue);margin-bottom:10px}
.trip-col p{font-size:13.3px;line-height:24px;margin-bottom:24px}
.form{position:absolute;left:81px;top:480px;width:760px;font-size:10.5px;color:#111}
.row{position:absolute;left:0;display:flex;align-items:flex-end;gap:4px;white-space:nowrap;width:760px}
.fill{flex:1;border-bottom:1px solid #111;height:11px}
.fill.w{flex:none}
.radio{display:inline-block;width:9px;height:9px;border:1px solid #111;border-radius:50%;margin:0 3px 0 8px;vertical-align:-1px}
.reg-head{position:absolute;top:31px;left:0;width:760px;text-align:center;font-size:16px;font-weight:700}
.tiny{font-size:6px;line-height:7px}
.optional{position:absolute;left:903px;top:557px;width:133px;height:119px;border:2px solid #111;padding:6px 10px;font-size:11px;line-height:16px;font-weight:600;color:#111}
.box{display:inline-block;width:12px;height:12px;border:1px solid #111;vertical-align:-2px;margin-right:2px}
.vdash{position:absolute;left:857px;top:520px;height:330px;border-left:1px dashed #aaa}
/* page 4 */
.p4{left:15px;top:2910px;width:1118px;height:863px}
.intro{position:absolute;left:81px;top:130px;width:985px;font-size:14.3px;line-height:25px}
.feature{position:absolute;top:258px;width:200px;text-align:center;font-size:17px;color:var(--ink)}
.feature svg{display:block;margin:0 auto 20px;width:84px;height:84px}
.cta{position:absolute;left:81px;top:480px;font-family:"Oswald",sans-serif;font-weight:500;font-size:34px;color:var(--blue)}
.band{position:absolute;left:0;top:520px;width:100%;height:343px;background:var(--band)}
.channel{position:absolute;top:95px;width:300px;text-align:center;color:var(--white)}
.channel svg{display:block;margin:0 auto 14px;width:70px;height:70px}
.channel h3{font-family:"Oswald",sans-serif;font-weight:300;font-size:32px;letter-spacing:1px;line-height:38px}
.channel p{font-size:15px;line-height:22px}
</style>
</head>
<body>

<!-- PAGE 1 -->
<section class="page p1">
  <div class="stripe"></div>
  <div class="brand" style="left:107px;top:46px;font-size:29px"><span class="brand-mark" style="width:40px;height:40px"></span>SUMMIT TRAILS</div>
  <h1 class="letter-title">Letter from teacher introductcing trip</h1>
  <p class="letter-salute">Dear Parents and Students</p>
  <div class="letter-body">
    <p class="lorem">Lorem Ipsum is simply dummy text of the printing and typesetting industry. Lorem Ipsum has been the industry's standard dummy text ever since the 1500s, when an unknown printer took a galley of type and scrambled it to make a type specimen book. It has survived not only five centuries, but also the leap into electronic typesetting, remaining essentially unchanged. It was popularised in the 1960s with the release of Lettersheet sheets containing Lorem Ipsum passages, and more recently with desktop publishing software like Layout Studio including versions of Lorem Ipsum.</p>
    <p class="lorem">Lorem Ipsum is simply dummy text of the printing and typesetting industry. Lorem Ipsum has been the industry's standard dummy</p>
    <p class="lorem">It has survived not only five centuries, but also the leap into electronic typesetting, remaining essentially unchanged. It was popularised in the 1960s with the release of Lettersheet sheets containing Lorem Ipsum passages</p>
  </div>
  <p class="letter-sign">Thanks &amp; Regards,<br>Name Here</p>

  <div class="info" style="left:107px;top:534px">
    <svg viewBox="0 0 62 62" fill="none" stroke="#8cc65a" stroke-width="2"><circle cx="31" cy="16" r="7"/><circle cx="13" cy="24" r="5"/><circle cx="49" cy="24" r="5"/><path d="M18 56V40a13 13 0 0 1 26 0v16M3 56V42a10 10 0 0 1 13-9M59 56V42a10 10 0 0 0-13-9"/></svg>
    <h3>Number Reference</h3><p>Include Trip number reference<br>for online registration</p>
  </div>
  <div class="info" style="left:442px;top:534px">
    <svg viewBox="0 0 62 62" fill="none" stroke="#8cc65a" stroke-width="2"><path d="M31 58C18 42 11 32 11 22a20 20 0 0 1 40 0c0 10-7 20-20 36z"/><circle cx="31" cy="22" r="7"/></svg>
    <h3>Destinations</h3><p>Include Trip number reference<br>for online registration</p>
  </div>
  <div class="info" style="left:828px;top:534px">
    <svg viewBox="0 0 62 62" fill="none" stroke="#8cc65a" stroke-width="2"><circle cx="31" cy="31" r="27"/><circle cx="31" cy="24" r="9"/><path d="M14 50a19 15 0 0 1 34 0"/></svg>
    <h3>Primary Group contact</h3><p>Include Trip number reference<br>for online registration</p>
  </div>
  <div class="info" style="left:107px;top:683px">
    <svg viewBox="0 0 62 62" fill="none" stroke="#8cc65a" stroke-width="2"><rect x="5" y="9" width="52" height="48" rx="3"/><path d="M5 21h52M17 4v10M45 4v10"/><rect x="12" y="28" width="10" height="8"/><rect x="26" y="28" width="10" height="8"/><rect x="40" y="28" width="10" height="8"/><rect x="12" y="41" width="10" height="8"/><rect x="26" y="41" width="10" height="8"/><rect x="40" y="41" width="10" height="8"/></svg>
    <h3>Dates</h3><p>May 25 - 28 2025<br>3 Days/4 nights</p>
  </div>
  <div class="info" style="left:442px;top:683px">
    <svg viewBox="0 0 62 62" fill="none" stroke="#8cc65a" stroke-width="2"><path d="M22 4h18l-4 10h-10zM24 14h14v6h-14zM21 20h20l4 8v28H17V28z"/><path d="M35 32c-2-2-8-2-8 2s8 3 8 7-6 4-8 2M31 29v3M31 45v3"/></svg>
    <h3>Prices</h3><p>Include Trip number reference<br>for online registration</p>
  </div>
  <div class="info" style="left:828px;top:683px">
    <div class="brand" style="position:relative;font-size:17px;gap:6px;margin:14px 0 22px"><span class="brand-mark" style="width:26px;height:26px"></span>SUMMIT TRAILS</div>
    <h3>Customer Service:</h3><p>help@summittrails.com<br>888-555-0142</p>
  </div>
</section>
<div class="page-label" style="left:0;width:1290px;top:887px">PAGE NO 01 (Horizontal)</div>

<!-- PAGE 2 -->
<section class="page p2">
  <div class="stripe" role="img" aria-label="Teal to green sidebar with a faint dot texture"></div>
  <div class="brand" style="left:96px;top:20px;font-size:13px;gap:5px;letter-spacing:2px"><span class="brand-mark" style="width:22px;height:22px"></span>SUMMIT TRAILS</div>
  <p class="itin-title">Sample 4 Day/3 Night NYC itinerary</p>
  <table class="itin">
    <tr><th>DAY 1</th><th>DAY 2</th><th>DAY 3</th><th>DAY 4</th></tr>
    <tr>
      <td>
        <p>Early Morning Departure for New York City</p>
        <p>Summit Trails (ST) Representative greets group upon arrival</p>
        <p>Introductory tour of NYC</p>
        <p><b>LUNCH included</b></p>
        <p style="padding-left:10px">Chinatown</p><p style="padding-left:10px">Little Italy</p><p style="padding-left:10px">SoHo &amp; Chelsea</p>
        <p><b>DINNER included</b></p>
        <p class="c">Skyscraper Observation Deck<br>or<br>Rooftop Observation Deck</p>
        <p><b>CHECK IN</b> NYC Hotel</p>
        <p>ST Representative handles pre-check in &amp; assists group upon arrival</p>
        <p class="c"><b>*Security on duty 10PM – 5AM*</b></p>
      </td>
      <td>
        <p><b>DEPART Hotel for Breakfast</b></p>
        <p class="c">Morning TV Show Taping<br>or<br>Breakfast TV Show Taping</p>
        <p style="padding-left:8px">Central Park<br>Strawberry Fields</p>
        <p><b>LUNCH included</b></p>
        <p class="c">Natural History Museum<br>or<br>City Art Museum</p>
        <p style="padding-left:8px">Midtown Plaza<br>St. Patrick's Cathedral</p>
        <p><b>DINNER included</b></p>
        <p class="c">Times Square or Waterfront Pier</p>
        <p><b>RETURN</b> to Hotel</p>
        <p class="c"><b>*Security on duty 10PM–5AM*</b></p>
      </td>
      <td>
        <p><b>DEPART Hotel for Breakfast</b></p>
        <p style="padding-left:8px">9/11 Memorial</p>
        <p style="padding-left:8px">Wall Street – Financial District</p>
        <p style="padding-left:8px">South Street Seaport</p>
        <p><b>LUNCH included</b></p>
        <p class="c">City Music Hall Tour<br>or<br>TV Studios Tour</p>
        <p>Back to hotel to change for Dinner &amp; Play</p>
        <p><b>DINNER included</b></p>
        <p style="padding-left:8px">Broadway Play</p>
        <p style="padding-left:8px">Group Photo on Times Square</p>
        <p><b>RETURN</b> to Hotel</p>
        <p class="c"><b>*Security on duty 11PM–5AM*</b></p>
      </td>
      <td>
        <p><b>CHECK OUT/ DEPART Hotel for B'fast</b></p>
        <p style="padding-left:8px">Statue of Liberty<br>Ellis Island</p>
        <p style="padding-left:8px">Battery Park</p>
        <p><b>LUNCH included</b></p>
        <p style="padding-left:8px">5th Avenue Shopping</p>
        <p><b>DINNER</b> (time permitting)</p>
        <p><b>DEPART</b> NYC for Home</p>
        <div class="note"><p>Summit Trails customizes each trip to the specifications and requests of the customer.</p><p style="margin:0">This is just a SAMPLE itinerary of a 4 Day / 3 Night trip to NYC</p></div>
      </td>
    </tr>
  </table>
  <div class="disclaimer">
    <h2>Desclaimer</h2>
    <p>Lorem ipsum dolor sit Lorem ipsum dolor sit Lorem ipsum dolor sit Lorem ipsum dolor sit Lorem ipsum dolor sit Lorem ipsum dolor sit Lorem ipsum dolor sit Lorem ipsum dolor sit Lorem ipsum dolor sit Lorem ipsum dolor sit Lorem ipsum dolor sit</p>
    <p class="gap">Lorem ipsum dolor sit Lorem ipsum dolor sit Lorem ipsum dolor sit Lorem ipsum dolor sitLorem ipsum dolor sit Lorem ipsum dolor sit Lorem ipsum dolor sit Lorem ipsum dolor sit Lorem ipsum dolor sit Lorem ipsum dolor sit Lorem ipsum dolor sit</p>
    <p class="gap">Lorem ipsum dolor sit Lorem ipsum dolor sit Lorem ipsum dolor sit Lorem ipsum dolor sit Lorem ipsum dolor sit Lorem ipsum dolor sit</p>
    <p>Lorem ipsum dolor sit Lorem ipsum dolor sit Lorem ipsum dolor sitLorem ipsum dolor sit Lorem ipsum dolor sit Lorem ipsum dolor sit Lorem ipsum dolor sit Lorem ipsum dolor sit Lorem ipsum dolor sit Lorem ipsum dolor sit Lorem ipsum dolor sit Lorem ipsum dolor sit Lorem ipsum dolor sit Lorem ipsum dolor sit Lorem ipsum dolor sit Lorem ipsum dolor sit Lorem ipsum dolor sit</p>
  </div>
</section>
<div class="page-label" style="left:843px;top:1540px;transform:translate(-50%,-50%) rotate(-90deg)">PAGE NO 02 (Landscape)</div>

<!-- PAGE 3 -->
<section class="page p3">
  <div class="stripe"></div>
  <div class="brand" style="left:81px;top:29px;font-size:29px"><span class="brand-mark" style="width:44px;height:44px"></span>SUMMIT TRAILS</div>
  <div class="trip-col" style="left:73px">
    <h2>Trip Details Title Here</h2>
    <p>Lorem ipsum dolor sit Lorem ipsum dolor sit Lorem ipsum dolor sit Lorem ipsum dolor sit Lorem ipsum dolor sit Lorem ipsum dolor sit Lorem ipsum dolor sit Lorem ipsum dolor sit Lorem ipsum dolor sit Lorem ipsum dolor sit Lorem ipsum dolor sit Lorem ipsum dolor sit</p>
    <p>Lorem ipsum dolor sit Lorem ipsum dolor sit Lorem ipsum dolor sit Lorem ipsum dolor sit Lorem ipsum dolor sit Lorem ipsum dolor sit Lorem ipsum dolor sit Lorem ipsum dolor sit Lorem ipsum dolor sit Lorem ipsum dolor sit Lorem ipsum dolor sit Lorem ipsum dolor sit</p>
  </div>
  <div class="trip-col" style="left:577px">
    <h2>Trip Details Title Here</h2>
    <p>Lorem ipsum dolor sit Lorem ipsum dolor sit Lorem ipsum dolor sit Lorem ipsum dolor sit Lorem ipsum dolor sit Lorem ipsum dolor sit Lorem ipsum dolor sit Lorem ipsum dolor sit Lorem ipsum dolor sit Lorem ipsum dolor sit Lorem ipsum dolor sit Lorem ipsum dolor sit</p>
    <p>Lorem ipsum dolor sit Lorem ipsum dolor sit Lorem ipsum dolor sit Lorem ipsum dolor sit Lorem ipsum dolor sit Lorem ipsum dolor sit Lorem ipsum dolor sit Lorem ipsum dolor sit Lorem ipsum dolor sit Lorem ipsum dolor sit Lorem ipsum dolor sit Lorem ipsum dolor sit</p>
  </div>
  <div class="dots" style="top:449px"></div>

  <div class="form">
    <div class="row" style="top:0;width:330px">Trip Date: <span class="fill"></span> For: <span class="fill"></span></div>
    <div class="reg-head">REGISTER ONLINE NOW <span style="font-weight:400;font-size:12px">at</span> <span style="font-size:18px">www.summittrails.com</span></div>
    <div class="row" style="top:56px">Registration Type: <span class="radio"></span>Student <span class="radio"></span>Adult <span style="margin-left:110px">Traveler's Date of Birth: ____ /___ /___</span><span style="margin-left:70px"><span class="radio"></span>Male <span class="radio"></span>Female</span></div>
    <div class="row" style="top:80px">Traveler's Full Legal Name: <span class="fill"></span></div>
    <div class="row tiny" style="top:93px;padding-left:200px">Full legal name must match the official travel document used for check-in.</div>
    <div class="row" style="top:117px">Parent/Guardian Name: <span class="fill"></span></div>
    <div class="row" style="top:135px">Mailing Address: <span class="fill"></span></div>
    <div class="row" style="top:154px">City: <span class="fill"></span> State: <span class="fill"></span> Zip: <span class="fill"></span></div>
    <div class="row" style="top:172px">Parent's Cell Phone: (<span class="fill w" style="width:40px"></span>) <span class="fill w" style="width:60px"></span>-<span class="fill w" style="width:70px"></span> Secondary Phone Number: (<span class="fill w" style="width:40px"></span>) <span class="fill"></span></div>
    <div class="row" style="top:192px">Parent/Legal Guardian Email: <span class="fill"></span></div>
    <div class="row" style="top:210px"><span class="radio" style="margin-left:0"></span>Enclosed is my check payable to <b style="font-size:11.5px;font-weight:600">www.summittrails.com</b> in the amount of $ <span class="fill w" style="width:90px"></span><span class="tiny">(Minimum payment required)</span></div>
    <div class="row" style="top:229px"><span class="radio" style="margin-left:0"></span>Pay by credit card: <span class="radio"></span>Northstar <span class="radio"></span>Meridian <span class="radio"></span>Keystone <span class="radio"></span>Apex</div>
    <div class="row" style="top:250px">Credit Card #: <span class="fill"></span> Amount to Charge: $ <span class="fill w" style="width:60px"></span> Exp.: ___ / ___ CVV: <span class="fill w" style="width:140px"></span></div>
    <div class="row" style="top:271px">Cardholder Name (print): <span class="fill"></span></div>
    <div class="row" style="top:290px">Signature: <span class="fill"></span></div>
    <div class="row tiny" style="top:309px;font-weight:600">By signing here, I have read and agree to www.summittrails.com's Terms &amp; Conditions at www.summittrails.com/terms.</div>
    <div class="row" style="top:323px;font-size:10px;align-items:flex-start;line-height:11px">Please Select: <span class="radio"></span><b style="font-size:8.5px;white-space:normal;width:280px">I AGREE to protect my payments with the Trip Cost Protection Program (recommended).</b><span class="radio"></span><b style="font-size:8.5px;white-space:normal;width:330px">I DECLINE to protect my payments with the Payment Trip Cost Protection understanding that I may lose my money if the trip is canceled for any reason.</b></div>
    <div class="row" style="top:364px;justify-content:flex-end;font-size:9px;font-weight:700;padding-right:30px">9811 / DK / 22</div>
  </div>
  <div class="row" style="left:870px;top:520px;width:170px;font-size:11px">Trip #: <span class="fill"></span></div>
  <div class="vdash"></div>
  <div class="optional">Optional<br>T-shirt : $25.00<br>Adults Sizes<br><span class="box"></span>S &nbsp;<span class="box"></span>M<span class="box"></span>S<br><span class="box"></span>XL &nbsp;<span class="box"></span>XXL</div>
</section>
<div class="page-label" style="left:0;width:1290px;top:2827px">PAGE NO 03 (Horizontal)</div>

<!-- PAGE 4 -->
<section class="page p4">
  <div class="stripe"></div>
  <div class="brand" style="left:81px;top:29px;font-size:29px"><span class="brand-mark" style="width:44px;height:44px"></span>SUMMIT TRAILS</div>
  <p class="intro">Lorem ipsum dolor sit Lorem ipsum dolor sit Lorem ipsum dolor sit Lorem ipsum dolor sit Lorem ipsum dolor sit Lorem ipsum dolor sit Lorem ipsum dolor sit Lorem ipsum dolor sit Lorem ipsum dolor sit Lorem ipsum dolor sit Lorem ipsum dolor sit Lorem ipsum dolor sit Lorem ipsum dolor sit Lorem ipsum dolor sit Lorem ipsum dolor sit Lorem ipsum dolor sit Lorem ipsum dolor sit Lorem ipsum dolor sit Lorem ipsum dolor sit Lorem ipsum dolor sit Lorem ipsum dolor sit Lorem ipsum dolor sit Lorem ipsum dolor sit Lorem ipsum dolor sit Lorem ipsum dolor sit</p>

  <div class="feature" style="left:42px">
    <svg viewBox="0 0 84 84" fill="none" stroke="#6bb5a6" stroke-width="2.5"><path d="M42 6l24 9v18c0 16-10 26-24 32C28 59 18 49 18 33V15z"/><path d="M31 34l8 8 14-15" stroke="#8cc65a"/><path d="M4 50l14 22h20M80 50L66 72H46"/></svg>Insurance</div>
  <div class="feature" style="left:263px">
    <svg viewBox="0 0 84 84" fill="none" stroke="#6bb5a6" stroke-width="2.5"><path d="M20 74C11 62 6 55 6 48a14 14 0 0 1 28 0c0 7-5 14-14 26z"/><circle cx="20" cy="48" r="5"/><path d="M64 40C56 30 52 24 52 18a12 12 0 0 1 24 0c0 6-4 12-12 22z" stroke="#8cc65a"/><circle cx="64" cy="18" r="4" stroke="#8cc65a"/><path d="M26 74h20c10 0 10-14 20-14h4" stroke-dasharray="4 4"/></svg>24/7 Tour Assistance</div>
  <div class="feature" style="left:480px">
    <svg viewBox="0 0 84 84" fill="#8cc65a"><circle cx="42" cy="14" r="10"/><path d="M28 50a14 16 0 0 1 28 0z" fill="#6bb5a6"/><path d="M16 58l4 8 9 1-7 6 2 9-8-5-8 5 2-9-7-6 9-1zM42 58l4 8 9 1-7 6 2 9-8-5-8 5 2-9-7-6 9-1zM68 58l4 8 9 1-7 6 2 9-8-5-8 5 2-9-7-6 9-1z"/></svg>Experience</div>
  <div class="feature" style="left:702px">
    <svg viewBox="0 0 84 84" fill="none" stroke="#6bb5a6" stroke-width="2.5"><path d="M24 80V34h36v46M6 80h72M14 80V50h10M70 80V50H60"/><path d="M32 44h6M46 44h6M32 56h6M46 56h6M36 80V68h12v12"/><path d="M42 8l3 6 6 1-4 4 1 6-6-3-6 3 1-6-4-4 6-1zM24 16l2 4 4 1-3 3 1 4-4-2-4 2 1-4-3-3 4-1zM60 16l2 4 4 1-3 3 1 4-4-2-4 2 1-4-3-3 4-1z" stroke="#8cc65a"/></svg>Brand Name Hotels</div>
  <div class="feature" style="left:922px">
    <svg viewBox="0 0 84 84" fill="none" stroke="#6bb5a6" stroke-width="2.5"><circle cx="50" cy="18" r="10" stroke="#8cc65a"/><path d="M44 26L30 44l4 4M34 40l4 4" stroke="#8cc65a"/><path d="M4 52h16l14 6h20c4 0 4 6 0 6H36M20 52v24M20 74h30l28-16c4-3 0-8-4-6L54 62"/></svg>Access</div>

  <div class="dots" style="top:447px"></div>
  <p class="cta">Sign up today for the trip of a lifetime!</p>

  <div class="band">
    <svg width="1118" height="120" viewBox="0 0 1118 120" style="position:absolute;left:0;top:70px" fill="none" stroke="#ffffff" stroke-opacity=".7" stroke-width="1.5" stroke-dasharray="6 6"><path d="M0 80C60 60 110 50 180 58M290 58C360 70 420 75 510 58M640 58C700 40 780 40 830 55M950 55C1020 45 1080 50 1118 70"/></svg>
    <div class="channel" style="left:79px">
      <svg viewBox="0 0 70 70" fill="none" stroke="#fff" stroke-width="2.5"><circle cx="35" cy="35" r="30"/><ellipse cx="35" cy="35" rx="13" ry="30"/><path d="M5 35h60M9 20h52M9 50h52M35 5v60"/></svg>
      <h3>ONLINE</h3><p>www.summittrails.com</p>
    </div>
    <div class="channel" style="left:422px">
      <svg viewBox="0 0 70 70" fill="none" stroke="#fff" stroke-width="2.5"><rect x="24" y="6" width="22" height="58" rx="4"/><path d="M31 12h8M33 57h4M14 24c-5 7-5 15 0 22M8 18c-9 11-9 23 0 34M56 24c5 7 5 15 0 22M62 18c9 11 9 23 0 34"/></svg>
      <h3>PHONE</h3><p>+01 555 0100 2 345</p>
    </div>
    <div class="channel" style="left:735px">
      <svg viewBox="0 0 70 70" fill="none" stroke="#fff" stroke-width="2.5"><rect x="4" y="14" width="62" height="42"/><path d="M4 14l31 24 31-24M4 56l24-20M66 56L42 36"/></svg>
      <h3>MAIL</h3><p>Fill out the attached form<br>and return by mail</p>
    </div>
  </div>
</section>
<div class="page-label" style="left:0;width:1290px;top:3820px">PAGE NO 04 (Horizontal)</div>

</body>
</html>
```